Kestrel Motorworks Card

Our company is an offroad fabrication shop that does everything from product installs to complete turnkey offroad racers. We are looking to generate new business cards for the 2014 Lords of the Canyon race in February. This is one of the largest offroad races in the country. We would like to see designs that incorporate the colors used in our logo - black, red, and white.

Industry/Entity Type

Shop

Contact Information for Business Card

KESTREL Motorworks, 2873 Marwood Ln. Houston, TX, 713-452-3071, www.kestrelmotorworks.example, Leon Farrowby, Owen Tilsley, Owners.

Requirements
Nice to have
• Would like to see the Logo full size on the back size of the car.

```html
<!DOCTYPE html>
<html lang="en">
<head>
<meta charset="utf-8">
<title>Kestrel Motorworks Business Card</title>
<link href="https://fonts.googleapis.com/css2?family=Open+Sans:ital,wght@0,400;0,600;0,700;0,800;1,400&display=swap" rel="stylesheet">
<style>
  :root {
    --red: #e8262b;
    --black: #111111;
    --charcoal: #2a2a2a;
    --white: #ffffff;
    --paper: #fbfbf9;
    --ink: #222222;
    --backdrop: #d6d6d6;
  }
  * { box-sizing: border-box; margin: 0; padding: 0; }
  html, body {
    width: 1200px;
    height: 1023px;
    overflow: hidden;
  }
  body {
    background: var(--backdrop);
    font-family: "Open Sans", Arial, sans-serif;
    position: relative;
  }
  .card {
    position: absolute;
    left: 250px;
    width: 700px;
    height: 400px;
    overflow: hidden;
    box-shadow: 0 6px 18px rgba(0,0,0,0.25);
  }
  .card-back { top: 60px; }
  .card-front { top: 520px; background: var(--paper); }

  .mud-texture {
    position: absolute;
    inset: 0;
    background:
      radial-gradient(ellipse at 50% 35%, #4a4845 0%, #2b2a28 45%, var(--black) 100%);
  }

  .brand-name {
    position: absolute;
    left: 0;
    right: 0;
    text-align: center;
    font-family: "Open Sans", Arial, sans-serif;
    font-weight: 800;
    color: var(--red);
    line-height: 1;
    letter-spacing: 1px;
  }
  .card-back .brand-name { top: 140px; font-size: 60px; }
  .card-front .brand-name { top: 52px; font-size: 52px; }

  .back-url {
    position: absolute;
    left: 0;
    right: 0;
    bottom: 34px;
    text-align: center;
    color: var(--white);
    font-size: 24px;
    font-weight: 400;
    letter-spacing: 0.5px;
  }

  .owners {
    position: absolute;
    top: 150px;
    left: 0;
    right: 0;
    text-align: center;
  }
  .owner-names {
    font-size: 30px;
    font-weight: 700;
    color: var(--ink);
    letter-spacing: 0.3px;
  }
  .owner-title {
    font-size: 19px;
    color: var(--red);
    margin-top: 2px;
  }

  .contact-band {
    position: absolute;
    left: 0;
    right: 0;
    bottom: 0;
    height: 150px;
  }
  .contact-band .mud-texture {
    background: linear-gradient(180deg, #1c1c1c 0%, #2d2c2a 50%, #151515 100%);
  }
  .contact-col {
    position: absolute;
    top: 38px;
    color: var(--white);
    font-size: 18px;
    font-style: italic;
    line-height: 1.35;
  }
  .contact-col.address { left: 95px; }
  .contact-col.reach { left: 390px; }
  .contact-row {
    display: flex;
    align-items: flex-start;
    gap: 12px;
  }
  .icon {
    flex: none;
    width: 20px;
    height: 20px;
    margin-top: 2px;
    background: var(--red);
    border-radius: 3px;
    display: flex;
    align-items: center;
    justify-content: center;
  }
  .icon svg { width: 14px; height: 14px; }
  .address-lines { display: block; }
</style>
</head>
<body>

  <section class="card card-back" aria-label="Card back">
    <div class="mud-texture" role="img" aria-label="Dark muddy ground with tire tracks"></div>
    <div class="brand-name">KESTREL Motorworks</div>
    <div class="back-url">www.kestrelmotorworks.example</div>
  </section>

  <section class="card card-front" aria-label="Card front">
    <div class="brand-name">KESTREL Motorworks</div>
    <div class="owners">
      <div class="owner-names">Leon Farrowby &amp; Owen Tilsley</div>
      <div class="owner-title">Owners</div>
    </div>

    <div class="contact-band">
      <div class="mud-texture" role="img" aria-label="Dark tire track texture"></div>

      <div class="contact-col address">
        <div class="contact-row">
          <span class="icon">
            <svg viewBox="0 0 24 24"><path fill="#fff" d="M12 2a7 7 0 0 0-7 7c0 5 7 13 7 13s7-8 7-13a7 7 0 0 0-7-7zm0 9.5A2.5 2.5 0 1 1 12 6.5a2.5 2.5 0 0 1 0 5z"/></svg>
          </span>
          <span class="address-lines">Kestrel Motorworks<br>2873 Marwood Ln.<br>Houston, TX</span>
        </div>
      </div>

      <div class="contact-col reach">
        <div class="contact-row">
          <span class="icon">
            <svg viewBox="0 0 24 24"><path fill="#fff" d="M6.6 10.8a15 15 0 0 0 6.6 6.6l2.2-2.2a1 1 0 0 1 1-.25 11.4 11.4 0 0 0 3.6.57 1 1 0 0 1 1 1V20a1 1 0 0 1-1 1A17 17 0 0 1 3 4a1 1 0 0 1 1-1h3.5a1 1 0 0 1 1 1c0 1.25.2 2.45.57 3.57a1 1 0 0 1-.25 1z"/></svg>
          </span>
          <span>713-452-3071</span>
        </div>
        <div class="contact-row">
          <span class="icon">
            <svg viewBox="0 0 24 24"><circle cx="12" cy="12" r="9" fill="none" stroke="#fff" stroke-width="2"/><path d="M3 12h18M12 3c3 3 3 15 0 18M12 3c-3 3-3 15 0 18" fill="none" stroke="#fff" stroke-width="1.6"/></svg>
          </span>
          <span>www.kestrelmotorworks.example</span>
        </div>
        <div class="contact-row">
          <span class="icon">
            <svg viewBox="0 0 24 24"><rect x="3" y="6" width="18" height="12" rx="1" fill="#fff"/><path d="M3 7l9 6 9-6" fill="none" stroke="#e8262b" stroke-width="1.8"/></svg>
          </span>
          <span>info@kestrelmotorworks.example</span>
        </div>
      </div>
    </div>
  </section>

</body>
</html>
```